Bright Acorns Business Card Design

Bright Acorns - Nurturing Outdoor Learning Places

Bright Acorns is a company that focuses on promoting the design, construction, consultation and support of natural, creative and organic play spaces for Early Childhood and learning environments.

We need a professional Business Card designed that is unique modern and creative. The Philosophy of the company is nostalgic so the business and will need to reflect this but also reflect that our ideas are modern and cutting edge.

The business card will need to be a talking point, by either having a unique size, quality and/or placement of logo or other quality.

I am more interested in using natural recycled paper, as this would reflect the philosophy of the company, but I open to seeing colour used creatively.
Updates

Hi Designers, Apologies, Could you please add www.brightacorns.com.au to the business card. Thanks very much.

Hi All, Thank you all for your submission thus far. Please note the fonts for used in the logo are: Ostrich Sans Black and Archer Semi Bold. If these could be considered for contact details, my name etc. Also please show the design on a recycled brown card if possible as this will be the type of card I will use when printing. Thanks so much.

Target Market(s)

Child Care Providers, Play Industry Professionals

Industry/Entity Type

Business

Contact Information for Business Card

Bright Acorns
Nurturing Outdoor Learning Places
Marlene Okafor
0419 862 304
marlene@brightacorns.com.au

Font styles to use
Sans Serif

Requirements
Must have
• The Logo and the Details plus the below phrase
• Bright Acorns - Nurturing Outdoor Learning Places
Nice to have
• A bit of colour, but not too much colour.
Should not have
• Not to have a white background, recycled brown card only

```html
<!DOCTYPE html>
<html lang="en">
<head>
<meta charset="utf-8">
<title>Bright Acorns Business Card Design</title>
<link href="https://fonts.googleapis.com/css2?family=Oswald:wght@600&family=Arvo:wght@700&family=Open+Sans:wght@400;700&display=swap" rel="stylesheet">
<style>
  :root {
    --kraft: #c8b598;
    --kraft-light: #d3c3a9;
    --ink: #1a1714;
    --ink-soft: #3a342d;
    --text-grey: #5b554d;
    --backdrop: #e4d6c4;
  }
  * { margin: 0; padding: 0; box-sizing: border-box; }
  html, body { width: 1200px; height: 800px; overflow: hidden; }
  body { background: var(--backdrop); position: relative; }

  .card {
    position: absolute;
    width: 540px;
    height: 310px;
    overflow: hidden;
    box-shadow: 0 6px 18px rgba(60, 45, 30, 0.25);
  }

  /* Contact side */
  .card-front { left: 30px; top: 245px; background: var(--kraft); }
  .brand {
    position: absolute; left: 52px; top: 38px;
    display: flex; align-items: center; gap: 12px;
  }
  .brand-dot { width: 30px; height: 30px; border-radius: 50%; background: var(--ink); }
  .brand-name {
    font-family: "Oswald", sans-serif; font-weight: 600;
    font-size: 40px; letter-spacing: 1px; color: var(--ink); line-height: 1;
  }
  .tagline {
    position: absolute; left: 96px; top: 88px;
    font-family: "Arvo", serif; font-weight: 700;
    font-size: 10px; letter-spacing: 1.5px; color: var(--ink-soft);
    text-transform: uppercase; line-height: 1.3;
  }
  .contact { position: absolute; left: 30px; top: 140px; list-style: none; }
  .contact li {
    display: flex; align-items: center; gap: 12px;
    font-family: "Open Sans", sans-serif; font-size: 13px; color: var(--text-grey);
    margin-bottom: 6px;
  }
  .contact svg { width: 13px; height: 13px; fill: var(--ink); }
  .rule { position: absolute; height: 1px; background: var(--ink-soft); }
  .rule-top { left: 30px; right: 30px; top: 190px; }
  .rule-bottom { left: 300px; right: 30px; top: 250px; }
  .person {
    position: absolute; right: 30px; top: 222px;
    font-family: "Open Sans", sans-serif; font-weight: 700;
    font-size: 19px; color: var(--ink);
  }
  .web-front {
    position: absolute; right: 30px; top: 258px;
    font-family: "Open Sans", sans-serif; font-size: 13px; color: var(--text-grey);
  }
  .band { position: absolute; left: 0; right: 0; bottom: 0; height: 30px; background: var(--ink); }

  /* Brand side */
  .card-back { left: 630px; top: 245px; background: var(--ink); }
  .tree-art {
    position: absolute; left: 10px; top: -20px; width: 300px; height: 320px;
    background: radial-gradient(closest-side, var(--kraft-light), var(--kraft) 65%, rgba(200,181,152,0) 100%);
  }
  .back-name {
    position: absolute; right: 30px; top: 190px;
    font-family: "Oswald", sans-serif; font-weight: 600;
    font-size: 34px; letter-spacing: 1px; color: var(--kraft); line-height: 1;
  }
  .back-tagline {
    position: absolute; right: 40px; top: 232px;
    font-family: "Arvo", serif; font-weight: 700;
    font-size: 9px; letter-spacing: 1.5px; color: var(--kraft);
    text-transform: uppercase; text-align: center; line-height: 1.3;
  }
  .web-back {
    position: absolute; right: 30px; top: 268px;
    font-family: "Open Sans", sans-serif; font-size: 13px; color: var(--kraft);
  }
</style>
</head>
<body>

<section class="card card-front" aria-label="Business card contact side">
  <div class="brand">
    <span class="brand-dot"></span>
    <span class="brand-name">BRIGHT ACORNS</span>
  </div>
  <p class="tagline">Nurturing Outdoor<br>Learning Places</p>

  <ul class="contact">
    <li>
      <svg viewBox="0 0 24 24" aria-hidden="true"><path d="M6.6 10.8a15 15 0 0 0 6.6 6.6l2.2-2.2a1 1 0 0 1 1-.25 11.4 11.4 0 0 0 3.6.6 1 1 0 0 1 1 1V20a1 1 0 0 1-1 1A17 17 0 0 1 3 4a1 1 0 0 1 1-1h3.5a1 1 0 0 1 1 1c0 1.25.2 2.45.6 3.6a1 1 0 0 1-.25 1z"/></svg>
      0419 862 304
    </li>
    <li>
      <svg viewBox="0 0 24 24" aria-hidden="true"><path d="M2 5h20v14H2zm2 2v.4l8 5 8-5V7zm0 2.8V17h16V9.8l-8 5z"/></svg>
      marlene@brightacorns.com.au
    </li>
  </ul>

  <div class="rule rule-top"></div>
  <p class="person">Marlene Okafor</p>
  <div class="rule rule-bottom"></div>
  <p class="web-front">www.brightacorns.com.au</p>
  <div class="band"></div>
</section>

<section class="card card-back" aria-label="Business card brand side">
  <div class="tree-art" role="img" aria-label="Kraft-toned illustration of a leafy tree with a child swinging from a branch"></div>
  <p class="back-name">BRIGHT ACORNS</p>
  <p class="back-tagline">Nurturing Outdoor<br>Learning Places</p>
  <p class="web-back">www.brightacorns.com.au</p>
</section>

</body>
</html>
```